Heronby Mortgage Capital Business Card

We need a business card design for our mortgage servicing company. In addition to servicing the loans of homeowners, we help homeowners with purchasing their homes and any mortgage refinancing. We would like to see designs that use the colors in the logo attached below (gold-ish yellow and navy blue), and any other design you deem fit! The design should communicate a simpler life with smart mortgages provided by Heronby.

```html
<!DOCTYPE html>
<html lang="en">
<head>
<meta charset="utf-8">
<title>Heronby Mortgage Capital – Business Card</title>
<link href="https://fonts.googleapis.com/css2?family=Montserrat:wght@400;600;700&display=swap" rel="stylesheet">
<style>
  :root {
    --navy: #231b55;
    --gold: #efb12d;
    --white: #ffffff;
    --paper: #f6f6f8;
    --backdrop: #e4e4e8;
    --ink-soft: #2b2b3a;
  }
  * { box-sizing: border-box; margin: 0; padding: 0; }
  html, body {
    width: 1200px; height: 1200px; overflow: hidden;
    background: var(--backdrop);
    font-family: "Montserrat", Arial, sans-serif;
  }
  .sheet {
    width: 1200px; height: 1200px;
    display: flex; flex-direction: column; align-items: center; justify-content: center;
    gap: 52px;
  }
  .card {
    position: relative;
    width: 900px; height: 514px;
    border-radius: 28px;
    overflow: hidden;
    box-shadow: 0 10px 30px rgba(0,0,0,0.18);
  }
  .card--front { background: linear-gradient(180deg, var(--white), var(--paper)); }
  .card--back { background: var(--navy); display: flex; align-items: center; justify-content: center; }
  .wave { position: absolute; inset: 0; width: 100%; height: 100%; }

  .brand {
    display: flex; align-items: center; gap: 12px;
    font-weight: 700; letter-spacing: 0.5px; white-space: nowrap;
  }
  .brand__dot { border-radius: 50%; flex: none; }
  .brand--front { position: absolute; right: 60px; top: 130px; font-size: 32px; color: var(--navy); }
  .brand--front .brand__dot { width: 18px; height: 18px; background: var(--gold); }
  .brand--back { font-size: 72px; color: var(--gold); }
  .brand--back .brand__dot { width: 34px; height: 34px; background: var(--white); }

  .contact { position: absolute; left: 70px; top: 140px; color: var(--navy); }
  .contact__name { font-size: 38px; font-weight: 700; line-height: 1; }
  .contact__role { font-size: 18px; font-weight: 400; color: var(--ink-soft); letter-spacing: 1px; margin-top: 4px; }
  .contact__list { list-style: none; margin-top: 14px; }
  .contact__item {
    display: flex; align-items: flex-start; gap: 12px;
    font-size: 19px; line-height: 26px; color: var(--ink-soft); margin-bottom: 2px;
  }
  .contact__icon { width: 20px; height: 20px; margin-top: 3px; flex: none; fill: var(--navy); }
</style>
</head>
<body>
<main class="sheet">

  <section class="card card--front" aria-label="Card front">
    <svg class="wave" viewBox="0 0 900 514" preserveAspectRatio="none" aria-hidden="true">
      <path transform="translate(0,-26)" fill="var(--gold)" d="M0 540 L0 470 C 200 420, 480 420, 680 330 C 790 280, 850 262, 900 255 L900 540 Z"/>
      <path transform="translate(0,-12)" fill="var(--white)" d="M0 540 L0 470 C 200 420, 480 420, 680 330 C 790 280, 850 262, 900 255 L900 540 Z"/>
      <path fill="var(--navy)" d="M0 514 L0 470 C 200 420, 480 420, 680 330 C 790 280, 850 262, 900 255 L900 514 Z"/>
    </svg>

    <div class="brand brand--front"><span class="brand__dot"></span>Heronby Mortgage</div>

    <div class="contact">
      <p class="contact__name">FULL NAME</p>
      <p class="contact__role">POSITION</p>
      <ul class="contact__list">
        <li class="contact__item">
          <svg class="contact__icon" viewBox="0 0 24 24"><path d="M6.6 10.8a15.2 15.2 0 0 0 6.6 6.6l2.2-2.2c.3-.3.7-.4 1-.2 1.1.4 2.3.6 3.6.6.6 0 1 .4 1 1V20c0 .6-.4 1-1 1A17 17 0 0 1 3 4c0-.6.4-1 1-1h3.5c.6 0 1 .4 1 1 0 1.3.2 2.5.6 3.6.1.3 0 .7-.2 1z"/></svg>
          (000) 000 0000
        </li>
        <li class="contact__item">
          <svg class="contact__icon" viewBox="0 0 24 24"><path d="M2 5h20v14H2z M3.5 6.5 12 13l8.5-6.5" fill="none" stroke="var(--navy)" stroke-width="2"/></svg>
          email@company.com
        </li>
        <li class="contact__item">
          <svg class="contact__icon" viewBox="0 0 24 24"><g fill="none" stroke="var(--navy)" stroke-width="1.8"><circle cx="12" cy="12" r="9.5"/><ellipse cx="12" cy="12" rx="4" ry="9.5"/><path d="M2.5 12h19M4 7h16M4 17h16"/></g></svg>
          www.company.com
        </li>
        <li class="contact__item">
          <svg class="contact__icon" viewBox="0 0 24 24"><path d="M12 2a7 7 0 0 0-7 7c0 5 7 13 7 13s7-8 7-13a7 7 0 0 0-7-7zm0 9.5A2.5 2.5 0 1 1 12 6.5a2.5 2.5 0 0 1 0 5z"/></svg>
          123 Name Street, 000<br>Your City, 00000-000
        </li>
      </ul>
    </div>
  </section>

  <section class="card card--back" aria-label="Card back">
    <div class="brand brand--back"><span class="brand__dot"></span>Heronby Mortgage</div>
  </section>

</main>
</body>
</html>
```